依頼詳細
・余白のある、落ち着いたデザインを希望です。
・以下参考サイトのような色味(キーカラー)を希望です。
(デザインは極端に類似しないことが望ましい)
- https://rinpa-kissa.jp/
- https://hamonoya.com/
・サイトのメニューは
-ごあいさつ
-会社案内・沿革
-事業内容
-納入実績
-お問い合わせ
-みなせのものづくり(ブログ)
-ネットショップ
となる予定です。
この度は、「TOPページのデザイン」と、上記「下層ページのベースデザイン」を依頼いたします。
・レスポンシブでスマートフォンにも対応させます。
・TOPページにはNEWS(お知らせ)欄が入る予定です。
・最終的に当方でWordPressにて構築します。
・参考サイトのイメージにとらわれない自由なデザインでもOKです。
ぜひ様々なアイデアをご提案下さい。
サイトURL
ページ数
2ページ
希望イメージ
シンプル 複雑
単色 カラフル
暗い 明るい
日常 高級
遊び心 厳粛
未来的 伝統的
女性的 男性的
希望する色
茶系、背景は白でお願いいたします。
納品ファイル
• 高解像度JPG (.jpg)
• イラストレーター形式 (.ai)
• フォトショップ形式 (.psd)
• PNG形式 (.png)
補足説明
資料と素材写真を添付いたします。
写真は今後差し替え予定なのでダミーとしてお使いください。

素材画像で購入が必要なものがある場合、「Pexel Vault (https://vault.pexelmart.com/jp/)」より選定下さい。当方で購入しますので、ご提案の際はカンプ画像を利用いただき、採用後には素材のURL or ファイル番号をお伝えいただきます。

その他ご不明な点がございましたら、お気軽にご連絡下さい。

シンプルで飽きの来ないデザインをクライアント様が気に入りました。

この度は本当にたくさんのご提案をいただきましてまことにありがとうございました。
どのデザインも素敵で、選ぶのに時間がかかりまして申し訳ございませんでした。
またの機会がございましたらご提案ください。改めて御礼申し上げます。

```html
<!DOCTYPE html>
<html lang="ja">
<head>
<meta charset="utf-8">
<title>みなせ工房</title>
<link rel="stylesheet" href="https://fonts.googleapis.com/css2?family=Shippori+Mincho:wght@400;600&family=Noto+Serif+JP:wght@400;600&display=swap">
<style>
:root{
  --ink:#2b2520;
  --text:#4a4039;
  --muted:#8a7f76;
  --brown:#7a5634;
  --line:#d9d2c8;
  --paper:#f4f0ea;
  --white:#ffffff;
  --footer:#262220;
}
*{box-sizing:border-box;margin:0;padding:0}
html,body{width:1200px;height:4048px;overflow:hidden}
body{background:var(--white);color:var(--text);font-family:"Noto Serif JP",serif;font-size:14px;position:relative}
.abs{position:absolute}
.serif{font-family:"Shippori Mincho",serif}

/* header */
.logo{left:0;width:1200px;top:18px;text-align:center;color:var(--ink)}
.logo .name{font-family:"Shippori Mincho",serif;font-size:34px;font-weight:600;letter-spacing:6px;line-height:1}
.logo .roman{font-size:11px;letter-spacing:3px;margin-top:6px;color:var(--muted)}
.util{right:40px;top:18px;display:flex;gap:18px;font-size:12px;color:var(--muted)}
.util span::before{content:"";display:inline-block;width:8px;height:8px;border:1px solid var(--muted);margin-right:6px;vertical-align:middle}
.gnav{left:0;width:1200px;top:112px;display:flex;justify-content:center;gap:0;font-size:14px;color:var(--ink)}
.gnav span{padding:0 32px;border-left:1px solid var(--line)}
.gnav span:last-child{border-right:1px solid var(--line)}

.hero{left:0;top:164px;width:1200px;height:456px;background:linear-gradient(100deg,#1c1714 0%,#3a2b20 40%,#6a5341 60%,#2a211b 100%)}
.hero-copy{left:470px;top:220px;color:#f4ece0;font-family:"Shippori Mincho",serif;font-size:30px;letter-spacing:8px;line-height:1.7;writing-mode:vertical-rl;height:300px}

/* headings */
.sec-title{left:0;width:1200px;text-align:center;font-family:"Shippori Mincho",serif;font-size:24px;color:var(--ink);letter-spacing:4px}
.sec-title::after{content:"";display:block;width:36px;height:1px;background:var(--brown);margin:16px auto 0}

/* news */
.news{left:200px;top:770px;width:800px;border-top:1px solid var(--line)}
.news li{list-style:none;display:flex;gap:60px;padding:20px 24px;border-bottom:1px solid var(--line);font-size:13px}
.news .date{color:var(--muted);width:90px}

.paper{left:0;width:1200px;background:var(--paper)}

/* about */
.block-title{font-family:"Shippori Mincho",serif;font-size:26px;color:var(--ink);letter-spacing:3px}
.block-text{font-size:14px;line-height:2.1;color:var(--text)}
.btn{display:inline-block;width:150px;height:36px;line-height:34px;text-align:center;border:1px solid var(--brown);color:var(--brown);font-size:12px;letter-spacing:2px;background:var(--white)}
.photo{border-radius:0}

/* services */
.svc{display:flex;align-items:center;justify-content:center;text-align:center;color:#fff}
.svc-label{background:rgba(255,255,255,.85);color:var(--ink);padding:12px 26px;font-family:"Shippori Mincho",serif}
.svc-label b{display:block;font-size:24px;font-weight:600;letter-spacing:4px}
.svc-label small{font-size:10px;letter-spacing:1px;color:var(--muted)}

/* blog */
.blog-cap{font-size:12px;line-height:1.8;color:var(--text);width:260px}

/* contact buttons */
.cta{height:64px;border:1px solid var(--brown);display:flex;align-items:center;justify-content:center;gap:12px;font-size:16px;color:var(--ink);letter-spacing:3px}
.fnav{left:0;width:1200px;top:3700px;display:flex;justify-content:center;font-size:13px;color:var(--ink)}
.fnav span{padding:0 28px;border-left:1px solid var(--line)}
.fnav span:last-child{border-right:1px solid var(--line)}
.footer{left:0;top:3760px;width:1200px;height:288px;background:var(--footer);color:#d8d0c6;text-align:center}
.footer .name{font-family:"Shippori Mincho",serif;font-size:32px;font-weight:600;letter-spacing:6px;color:#fff;margin-top:50px}
.footer .roman{font-size:11px;letter-spacing:3px;margin-top:6px;color:#a89e94}
.footer .addr{font-size:12px;margin-top:26px;line-height:2}
.footer .copy{font-size:11px;color:#8a8079;margin-top:40px}
</style>
</head>
<body>

<header>
  <div class="abs logo"><div class="name">みなせ工房</div><div class="roman">Minase Kobo</div></div>
  <div class="abs util"><span>お問い合わせ</span><span>ネットショップ</span></div>
  <nav class="abs gnav"><span>ごあいさつ</span><span>会社案内・沿革</span><span>事業内容</span><span>納入実績</span><span>みなせのものづくり</span></nav>
</header>

<div class="abs hero" role="img" aria-label="職人が手で木型を彫っている作業場の写真"></div>
<div class="abs hero-copy">木型に<br>あなたの<br>思いをかたちに</div>

<section>
  <h2 class="abs sec-title" style="top:690px">お知らせ</h2>
  <ul class="abs news">
    <li><span class="date">2017.10.20</span><span>新しい木型のご案内を掲載しました。工房の見学も受付中です。</span></li>
    <li><span class="date">2017.10.10</span><span>年末年始の営業日についてのお知らせを掲載しました。</span></li>
    <li><span class="date">2017.10.01</span><span>ネットショップに新商品を追加しました。ぜひご覧ください。</span></li>
  </ul>
</section>

<div class="abs paper" style="top:1000px;height:1000px"></div>
<section>
  <div class="abs" style="left:296px;top:1070px;width:320px">
    <h3 class="block-title">みなせ工房とは</h3>
    <p class="block-text" style="margin-top:30px">伝統の技を受け継ぐ木型工房として、菓子木型や看板、造形物まで幅広く手がけております。一つひとつ丁寧に、お客様の思いをかたちにいたします。</p>
    <a class="btn" style="margin-top:40px">ごあいさつ</a>
  </div>
  <div class="abs photo" style="left:640px;top:1060px;width:300px;height:260px;background:linear-gradient(135deg,#8a6a4c,#d8c7ae 55%,#6e5238)" role="img" aria-label="木枠の中に置かれた菓子木型の写真"></div>

  <div class="abs photo" style="left:260px;top:1380px;width:300px;height:340px;background:linear-gradient(160deg,#3a2418,#a5452a 45%,#d9a35a 70%,#2b1c14)" role="img" aria-label="祭りの山車と飾り人形の写真"></div>
  <div class="abs" style="left:640px;top:1430px;width:300px">
    <h3 class="block-title">高度な技術とデザイン</h3>
    <p class="block-text" style="margin-top:30px">長年培った彫刻技術とデザイン力で、祭りの装飾から看板まで、細部までこだわった品をお届けします。</p>
    <a class="btn" style="margin-top:40px">事業内容</a>
  </div>
</section>

<section>
  <h2 class="abs sec-title" style="top:2060px">事業内容</h2>
  <div class="abs svc" style="left:192px;top:2128px;width:400px;height:224px;background:linear-gradient(135deg,#2a2420,#6b5a4a 50%,#d6cbbd)" role="img" aria-label="木型と木工品の写真"><div class="svc-label"><b>木型 木工</b><small>wooden mold / woodwork</small></div></div>
  <div class="abs svc" style="left:612px;top:2128px;width:396px;height:224px;background:linear-gradient(135deg,#7a1a1a,#b02a2a 50%,#8a1c1c)" role="img" aria-label="赤い布の上の菓子木型の写真"><div class="svc-label"><b>お菓子 木型</b><small>japanese sweets wooden mold</small></div></div>
  <div class="abs svc" style="left:192px;top:2380px;width:400px;height:220px;background:linear-gradient(135deg,#b79a7a,#e4d6c2 50%,#a88666)" role="img" aria-label="木彫りのはんこと彫刻の写真"><div class="svc-label"><b>アート造形 彫刻</b><small>art molding / sculpture</small></div></div>
  <div class="abs svc" style="left:612px;top:2380px;width:396px;height:220px;background:linear-gradient(135deg,#3a2a1c,#9c7a52 50%,#5a4128)" role="img" aria-label="木製の看板の写真"><div class="svc-label"><b>看板 デザイン</b><small>signboard design</small></div></div>
  <div class="abs svc" style="left:402px;top:2628px;width:400px;height:212px;background:linear-gradient(135deg,#1e2a44,#5a6a8a 50%,#2a3552)" role="img" aria-label="祭りの伝統芸能の写真"><div class="svc-label"><b>祭り 伝統芸能</b><small>festival / traditional arts</small></div></div>
</section>

<div class="abs paper" style="top:2940px;height:580px"></div>
<section>
  <h2 class="abs sec-title" style="top:2990px">みなせのものづくり</h2>
  <div class="abs" style="left:300px;top:3060px;width:200px;height:200px;background:linear-gradient(135deg,#f2efe9,#c9a040 55%,#e8e2d8)" role="img" aria-label="木製のスプーンの写真"></div>
  <div class="abs" style="left:500px;top:3060px;width:200px;height:200px;background:linear-gradient(135deg,#2a1c16,#a8402a 50%,#d9b070)" role="img" aria-label="祭りの飾り人形の写真"></div>
  <div class="abs" style="left:760px;top:3060px;width:200px;height:200px;background:linear-gradient(135deg,#8a5a3a,#d8a878 50%,#a06a44)" role="img" aria-label="彫りかけの木材の写真"></div>
  <p class="abs blog-cap" style="left:300px;top:3276px;width:190px">木のスプーンを制作しました。手に馴染む形です。</p>
  <p class="abs blog-cap" style="left:500px;top:3276px;width:190px">祭りの飾りを納品しました。色鮮やかな仕上がりです。</p>
  <p class="abs blog-cap" style="left:760px;top:3276px;width:190px">新しい木型の制作過程をご紹介します。</p>
  <a class="abs btn" style="left:525px;top:3364px">一覧を見る</a>
</section>

<section>
  <div class="abs cta" style="left:192px;top:3548px;width:400px">
    <svg width="20" height="14" viewBox="0 0 20 14"><rect x="0.5" y="0.5" width="19" height="13" fill="none" stroke="#7a5634"/><path d="M1 1l9 7 9-7" fill="none" stroke="#7a5634"/></svg>お問い合わせ</div>
  <div class="abs cta" style="left:612px;top:3548px;width:396px">
    <svg width="20" height="18" viewBox="0 0 20 18"><path d="M1 1h3l3 11h10l2-8H5" fill="none" stroke="#7a5634"/><circle cx="8" cy="16" r="1.5" fill="#7a5634"/><circle cx="16" cy="16" r="1.5" fill="#7a5634"/></svg>オンラインショップ</div>
</section>

<nav class="abs fnav"><span>ごあいさつ</span><span>会社案内・沿革</span><span>事業内容</span><span>納入実績</span><span>みなせのものづくり</span></nav>

<footer class="abs footer">
  <div class="name">みなせ工房</div>
  <div class="roman">Minase Kobo</div>
  <div class="addr">〒000-0000 架空県みなせ市木型町1-2-3<br>TEL : 0000-00-0000</div>
  <div class="copy">Copyright 2017 © Minase Kobo All Rights Reserved.</div>
</footer>

</body>
</html>
```